Wren Vehicle Polishing (Mobile detail)

I need a business card made up. I'd like it to be different in some form, either raised, embossed, debossed, something cool that stands out. (preferably embossed text somewhere in it). I will be including the Initial png file. Let me know if you need the photoshop of adobe illustrator file to work with.

Information to be included: Text: XXX-XXX-XXXX Phone: XXX-XXX-XXXX Email: wrenpolishcrew@mailbox-demo.net Website: www.socialpage-demo.net/wrenpolishKTR Hours of operation: Mon - Fri 7:00AM to 8:00PM Sat - 10:00AM to 8:00PM

Target Market(s)

Mobile automotive detailing

Industry/Entity Type

Automotive

Contact Information for Business Card

Make it stand out with embossed lettering, I'd also like the background to be glossy black or matte, something that represents a shiny car, black preferred

Requirements
Must have
• A glossy background, or something.
• My logo, pick one of them that best fits your design.
Should not have
• White background,
• something that does not stand out.

```html
<!DOCTYPE html>
<html lang="en">
<head>
<meta charset="utf-8">
<title>Wren Vehicle Polishing – Business Card</title>
<link href="https://fonts.googleapis.com/css2?family=Source+Sans+3:wght@400;600&display=swap" rel="stylesheet">
<style>
  :root {
    --canvas: #2b2724;
    --card-black: #0d0d0e;
    --card-edge: #1c1c1e;
    --accent: #e8501e;
    --text-light: #e6e6e6;
    --text-muted: #b9b9b9;
    --divider: #5a5a5a;
    --brand-silver: #d9d9db;
  }
  * { margin: 0; padding: 0; box-sizing: border-box; }
  html, body {
    width: 1200px; height: 814px; overflow: hidden;
    background: var(--canvas);
    font-family: "Source Sans 3", "Myriad Pro", Arial, sans-serif;
  }
  .sheet {
    position: relative; width: 1200px; height: 814px;
    display: flex; align-items: center; justify-content: center; gap: 40px;
  }
  .card {
    position: relative; width: 540px; height: 309px;
    background: radial-gradient(ellipse at 30% 20%, #1a1a1c 0%, var(--card-black) 70%);
    border: 1px solid var(--card-edge);
    box-shadow: 0 10px 28px rgba(0,0,0,.45);
  }
  /* brand name stands in for the mark */
  .brand {
    display: flex; align-items: center; gap: 10px;
    color: var(--brand-silver); font-weight: 600; line-height: 1.05;
  }
  .brand-dot {
    flex: none; width: 14px; height: 14px; border-radius: 50%;
    background: var(--accent);
  }
  /* front */
  .card-front .brand {
    position: absolute; left: 42px; top: 110px; width: 180px;
    font-size: 25px;
  }
  .card-front .divider {
    position: absolute; left: 240px; top: 72px; width: 1px; height: 160px;
    background: var(--divider);
  }
  .contact { position: absolute; left: 262px; top: 76px; }
  .contact-name { color: var(--accent); font-weight: 600; font-size: 19px; line-height: 1.1; }
  .contact-role { color: var(--text-muted); font-size: 14px; margin: 3px 0 8px; }
  .contact-list { list-style: none; }
  .contact-list li {
    display: flex; align-items: center; gap: 9px;
    color: var(--text-light); font-size: 14px; line-height: 20px;
  }
  .contact-list svg { flex: none; width: 12px; height: 12px; fill: var(--accent); }
  /* back */
  .card-back .brand {
    position: absolute; left: 50%; top: 64px; transform: translateX(-50%);
    font-size: 30px; white-space: nowrap;
  }
  .hours { position: absolute; left: 0; right: 0; top: 176px; text-align: center; }
  .hours-title { color: var(--accent); font-weight: 600; font-size: 15px; letter-spacing: .3px; }
  .hours-line { color: var(--text-light); font-size: 14px; margin-top: 4px; }
  .hours-sep { color: var(--accent); margin: 0 4px; }
</style>
</head>
<body>
<main class="sheet">
  <section class="card card-front" aria-label="Business card front">
    <div class="brand"><span class="brand-dot"></span><span>Wren Vehicle Polishing</span></div>
    <div class="divider"></div>
    <div class="contact">
      <p class="contact-name">Marcus Hale</p>
      <p class="contact-role">Detailer</p>
      <ul class="contact-list">
        <li>
          <svg viewBox="0 0 12 12" aria-hidden="true"><path d="M3 0h6a1 1 0 0 1 1 1v10a1 1 0 0 1-1 1H3a1 1 0 0 1-1-1V1a1 1 0 0 1 1-1zm0 1.5v8h6v-8z"/></svg>
          555-201-4837
        </li>
        <li>
          <svg viewBox="0 0 12 12" aria-hidden="true"><path d="M2.4.5l1.8 2.4-1 1.2c.7 1.6 2 2.9 3.6 3.6l1.2-1 2.4 1.8-.9 2.1C5 12 0 7 .3 1.4z"/></svg>
          555-309-7621
        </li>
        <li>
          <svg viewBox="0 0 12 12" aria-hidden="true"><path d="M0 2h12v8H0zm1.2 1L6 6.4 10.8 3z"/></svg>
          wrenpolishcrew@mailbox-demo.net
        </li>
        <li>
          <svg viewBox="0 0 12 12" aria-hidden="true"><rect x="0" y="0" width="12" height="12" rx="1.5"/></svg>
          /wrenpolishKTR
        </li>
      </ul>
    </div>
  </section>

  <section class="card card-back" aria-label="Business card back">
    <div class="brand"><span class="brand-dot"></span><span>Wren Vehicle Polishing</span></div>
    <div class="hours">
      <p class="hours-title">HOURS OF OPERATION</p>
      <p class="hours-line">Mon - Fri 7:00AM to 8:00PM<span class="hours-sep">|</span>Sat - 10:00AM to 8:00PM</p>
    </div>
  </section>
</main>
</body>
</html>
```